Business Card

Need a clean, professional, simple, but clever business card for our company ZOLT RIDES. We only want to see black and white colors as that reflects the branding of our company. Attaching logo. Will also consider the "sky blue" shown in our web site sample png - but use of the color should be minimal.

Zolt Rides is a executive car service operating in cities throughout Africa. By operating well equipped Vantorel Kess vehicles, we offer the smoothest and stylish ride in town. We aim to provide customers with a valuable experience. That’s why we make sure our patrons get picked up like a boss, travel in style, and arrive fabulous.

We need a card that says that. Likely to print on the best quality/smoothest paper available, as it must speak volumes of our business and class.

We would like the rear of the card to be all black. Perhaps we can put the web url on it, or leave it blank if it looks neater/more elegant.

Use the following contact information (as you see fit):

Zolt Rides Limited
P.O. Box 58146
Dar es Salaam, Tanzania

Baraka Nyerenda
Managing Director

+255 (0) 754 829067
sales@zoltrides.example

web url: www.zoltrides.example
email: chauffeur@zoltrides.example

***Winning designer will likely be commissioned for more promotional work in near future.

Target Market(s)

The target market for this card is corporate executives of top firms (financial, consulting, businessmen, etc). They are interested in high quality transportation. Our fleet is all high end Vantorel Kess black cars (black exterior, black interior); and therefore, that high end quality and promptness must be reflected in the card. Also simplicity, as we we take care of all the little details behind the scene.

Industry/Entity Type

Business

Requirements
Must have
• Font must be: Helvetica Neue, like the logo. You may use other variations (Thin, Ultra thin, Regular, Bold), so long as it looks and prints well.

If web url is included on the back of the card, then do NOT include it also on the front.
Nice to have
• If there is something nice and clever that you can do/think of that doesn't make the card look busy, but adds a little "posh", then I could be even more interested.

However, if there's no little thing do be done, I'd rather a simple, but very professional looking card that attracts a lot of attention.

```html
<!DOCTYPE html>
<html lang="en">
<head>
<meta charset="utf-8">
<title>Zolt Rides — Business Card</title>
<link rel="stylesheet" href="https://fonts.googleapis.com/css2?family=Arimo:wght@400&family=Poppins:wght@600&family=Questrial&display=swap">
<style>
  :root {
    --canvas-bg: #e6e6e6;
    --card-white: #ffffff;
    --card-black: #111719;
    --ink-black: #111111;
    --ink-white: #ffffff;
    --sky-blue: #5bc3e6;
  }
  * { box-sizing: border-box; margin: 0; padding: 0; }
  html, body {
    width: 1200px;
    height: 735px;
    overflow: hidden;
    background: var(--canvas-bg);
  }
  .canvas {
    position: relative;
    width: 1200px;
    height: 735px;
    display: flex;
    align-items: center;
    justify-content: center;
    gap: 50px;
  }
  .card {
    position: relative;
    width: 540px;
    height: 309px;
    box-shadow: 0 6px 18px rgba(0, 0, 0, 0.18);
  }
  .card--front { background: var(--card-white); }
  .card--back { background: var(--card-black); }

  .holder {
    position: absolute;
    top: 34px;
    right: 34px;
    text-align: right;
  }
  .holder__name {
    font-family: "Poppins", sans-serif;
    font-weight: 600;
    font-size: 27px;
    line-height: 1.1;
    color: var(--ink-black);
    letter-spacing: 0.2px;
  }
  .holder__title {
    font-family: "Questrial", sans-serif;
    font-size: 16px;
    color: var(--sky-blue);
    margin-top: 2px;
  }
  .contact {
    position: absolute;
    left: 34px;
    bottom: 30px;
    font-family: "Questrial", sans-serif;
    font-size: 19px;
    line-height: 1.2;
    color: var(--ink-black);
  }

  .brand {
    position: absolute;
    inset: 0;
    display: flex;
    flex-direction: column;
    align-items: center;
    justify-content: center;
    text-align: center;
  }
  .brand__name {
    font-family: "Arimo", sans-serif;
    font-weight: 400;
    font-size: 50px;
    line-height: 1;
    color: var(--ink-white);
    letter-spacing: 0.5px;
  }
  .brand__url {
    font-family: "Arimo", sans-serif;
    font-size: 19px;
    color: var(--ink-white);
    margin-top: 12px;
    margin-left: 90px;
  }
</style>
</head>
<body>
  <main class="canvas">
    <section class="card card--front" aria-label="Card front">
      <div class="holder">
        <p class="holder__name">Baraka Nyerenda</p>
        <p class="holder__title">Managing Director</p>
      </div>
      <div class="contact">
        <p class="contact__phone">+255 (0) 754 829067</p>
        <p class="contact__email">sales@zoltrides.example</p>
      </div>
    </section>

    <section class="card card--back" aria-label="Card back">
      <div class="brand">
        <p class="brand__name">ZOLT RIDES</p>
        <p class="brand__url">www.zoltrides.example</p>
      </div>
    </section>
  </main>
</body>
</html>
```